VEK.PRO- Daniel Whitcombe Fitness- needs a clever business card using the logo, name, info, contact

I need a business card designed for my Online Personal Training company called VEK.PRO, abbreviation for Daniel Whitcombe Fitness. My company focuses on coaching in personal health and personal growth to unleash your greatest potential. I would like to see designs that use my color scheme of a redish-orange (C:0,M:84,Y:100,K:0), grey, white, black, and my company font is OSWALD. The final design should communicate some aspects of design, health, motivation, growth, in some way. The logo is very important to the company and can be displayed in any of the colors previously mentioned. Must include the company name, my website: www.vek.example , my email: dan@vek.example

Target Market(s)

Personal health, fitness, general public, those who lack knowledge, awareness, and confidence in personal health

Industry/Entity Type

Personal Trainer

Font styles to use
Other font styles liked:
• OSWALD. (Bold, Regular, Light)

Colors
f37122
ffffff
9d9d9d
000000

Requirements
Must have
• Must include the logo, company name, my website: www.vek.example , my email: dan@vek.example
Nice to have
• Variations of the colors scheme of a redish-orange (C:0,M:84,Y:100,K:0), grey, white, black. Logo, card, or text can be in any of these colors.
• Possible quote like "Take control of your personal health to unleash your greatest potential" or "Unleashing your greatness first begins with fitness of the body and mind"

```html
<!DOCTYPE html>
<html lang="en">
<head>
<meta charset="utf-8">
<title>Daniel Whitcombe Fitness – Business Card</title>
<link rel="stylesheet" href="https://fonts.googleapis.com/css2?family=Oswald:wght@300;400&display=swap">
<style>
  :root {
    --page-bg: #e9e9e9;
    --card-bg: #ffffff;
    --rust: #c65a38;
    --rust-1: #c65a38;
    --rust-2: #cc6444;
    --rust-3: #d26f50;
    --rust-4: #d87b5d;
    --rust-5: #dd876b;
    --rust-6: #e29479;
    --icon-box: #4d4d4d;
    --ink: #3a3a3a;
    --white: #ffffff;
  }
  * { box-sizing: border-box; margin: 0; padding: 0; }
  html, body {
    width: 1200px; height: 800px; overflow: hidden;
    background: var(--page-bg);
    font-family: "Oswald", sans-serif;
  }
  .stage {
    width: 1200px; height: 800px;
    display: flex; align-items: center; justify-content: center;
  }
  .business-card {
    position: relative;
    width: 1000px; height: 540px;
    background: var(--card-bg);
    box-shadow: 0 10px 30px rgba(0,0,0,0.12);
  }
  .contact-list {
    position: absolute;
    left: 0; top: 140px;
    width: 480px;
    list-style: none;
  }
  .contact-row {
    display: flex; align-items: stretch;
    height: 44px;
    margin-bottom: 2px;
  }
  .contact-row:nth-child(1) { background: var(--rust-1); }
  .contact-row:nth-child(2) { background: var(--rust-2); }
  .contact-row:nth-child(3) { background: var(--rust-3); }
  .contact-row:nth-child(4) { background: var(--rust-4); }
  .contact-row:nth-child(5) { background: var(--rust-5); }
  .contact-row:nth-child(6) { background: var(--rust-6); }
  .contact-text {
    flex: 1;
    display: flex; align-items: center; justify-content: flex-end;
    padding-right: 10px;
    color: var(--white);
    font-weight: 300;
    font-size: 19px;
    letter-spacing: 0.02em;
  }
  .contact-icon {
    width: 44px;
    background: var(--icon-box);
    display: flex; align-items: center; justify-content: center;
    border-left: 2px solid var(--white);
  }
  .contact-icon svg { width: 24px; height: 24px; }
  .brand {
    position: absolute;
    left: 510px; top: 160px;
    display: flex; align-items: center;
    gap: 36px;
  }
  .brand-mark {
    width: 210px; height: 210px;
    border-radius: 50%;
    border: 12px solid var(--rust);
    flex: none;
  }
  .brand-name {
    color: var(--ink);
    font-weight: 300;
    font-size: 34px;
    line-height: 46px;
    letter-spacing: 0.18em;
    text-transform: uppercase;
  }
  .brand-name span { display: block; }
</style>
</head>
<body>
<main class="stage">
  <section class="business-card">
    <ul class="contact-list">
      <li class="contact-row">
        <span class="contact-text">55.010.020.030</span>
        <span class="contact-icon">
          <svg viewBox="0 0 24 24" aria-hidden="true"><path d="M7 3l3 4-2 2c1 2.5 3.5 5 6 6l2-2 4 3-2 4C11 20 4 13 3 5z" fill="none" stroke="#fff" stroke-width="1.6" stroke-linejoin="round"/></svg>
        </span>
      </li>
      <li class="contact-row">
        <span class="contact-text">dan@vek.example</span>
        <span class="contact-icon">
          <svg viewBox="0 0 24 24" aria-hidden="true"><rect x="3" y="6" width="18" height="12" fill="none" stroke="#fff" stroke-width="1.6"/><path d="M3 6l9 7 9-7" fill="none" stroke="#fff" stroke-width="1.6"/></svg>
        </span>
      </li>
      <li class="contact-row">
        <span class="contact-text">www.vek.example</span>
        <span class="contact-icon">
          <svg viewBox="0 0 24 24" aria-hidden="true"><circle cx="12" cy="12" r="8.5" fill="none" stroke="#fff" stroke-width="1.5"/><ellipse cx="12" cy="12" rx="3.8" ry="8.5" fill="none" stroke="#fff" stroke-width="1.3"/><path d="M3.5 12h17M5 7.5h14M5 16.5h14" stroke="#fff" stroke-width="1.3"/></svg>
        </span>
      </li>
      <li class="contact-row">
        <span class="contact-text">circle.example/vekpro</span>
        <span class="contact-icon">
          <svg viewBox="0 0 24 24" aria-hidden="true"><rect x="7" y="7" width="10" height="10" fill="#fff"/></svg>
        </span>
      </li>
      <li class="contact-row">
        <span class="contact-text">chirp.example/vekpro</span>
        <span class="contact-icon">
          <svg viewBox="0 0 24 24" aria-hidden="true"><rect x="7" y="7" width="10" height="10" fill="#fff"/></svg>
        </span>
      </li>
      <li class="contact-row">
        <span class="contact-text">network.example/vekpro</span>
        <span class="contact-icon">
          <svg viewBox="0 0 24 24" aria-hidden="true"><rect x="7" y="7" width="10" height="10" fill="#fff"/></svg>
        </span>
      </li>
    </ul>

    <div class="brand">
      <div class="brand-mark" aria-hidden="true"></div>
      <h1 class="brand-name">
        <span>Daniel</span>
        <span>Whitcombe</span>
        <span>Fitness</span>
      </h1>
    </div>
  </section>
</main>
</body>
</html>
```